Australia-Wide Industry Leader Bookkeeping Business Website Design Required

We need a website designed for our 10 year old bookkeeping business, Linden & Crane. Linden & Crane has been servicing the local & interstate communities of Australia, providing first-class BAS & Bookkeeping services with a personal touch unmatched by anyone else in the county.

What began 10 years ago as a small business focusing on family, friends and the local community, it has since grown into a well respected business with 95% of their business based solely on word of mouth and personal referrals from around Australia.

We would like to see designs that incorporate our existing brand/logo. The colours to be used on the website should be colours that work well with our logo. The design should communicate maturity, trust and confidence with a Web 2.0 look and feel.

We have produced mockups of the entire website as well as assets used in the mockups. Please reference the attached files. The mockups are an example of all the design elements that we want on each page. Designers are encouraged to use the mockups as a guideline only and for designers to use their own creativity.
Updates

This message is for new graphic designers who are considering commencing work on this project. Thank you for expressing an interest in our project. We would like to inform you that this project is close to completion as we have a number designs under very serious consideration.

We are currently in a position where we are disinterested providing feedback to improve on new designs submitted. We will provide feedback to improve new designs only if the submitted designs are very close to what we want for our website, and will only require 1 or 2 revision rounds to refine before the project completion date we will not work with designers to refine their newly submitted designs.

We feel that it is important for all designers to know the above information as we feel that your time and effort may be better spent working on another project.

Thank you for your understanding.

A big thank you for all the designs submitted. We are now in the process of selecting a design. Please be patient during this process. Thank you.

Target Market(s)

Busy Business Owners

Industry/Entity Type

Small Business

Requirements
Must have
• We require a rectangular "slide show" type feature to serve as a "teaser" to arouse the emotions of our website visitors. Each slide asks a specific question. The questions are:

- Is your paperwork in a mess?
- Do you need to get organised for the end of financial year?
- Are you sick & tired of endless amounts of paperwork & BASs?
- Do you feel frustrated & annoyed because you know your books need to be done?
- Do you lack the time & patience to get your paperwork done?
- Do you wish you had more time to do the things you enjoy doing?
- Contact Linden & Crane today and we will transform your chaos into order.

Underneath the slide show will be a button to "Call Linden & Crane Now - 03 7482 9163".

```html
<!DOCTYPE html>
<html lang="en">
<head>
<meta charset="utf-8">
<title>Linden &amp; Crane</title>
<link rel="stylesheet" href="https://fonts.googleapis.com/css2?family=Arimo:wght@400;700&family=Noto+Serif:wght@400&family=PT+Sans+Narrow:wght@700&family=Ubuntu:wght@700&family=Open+Sans:wght@800&display=swap">
<style>
:root{
  --orange:#e45f22;
  --dark:#262626;
  --dark-2:#303030;
  --panel:#dcdfe1;
  --text:#555;
  --head:#1c1c1c;
  --header-a:#f4f4f4;
  --header-b:#c9c9c9;
  --white:#fff;
}
*{margin:0;padding:0;box-sizing:border-box}
html,body{width:681px;height:1200px;overflow:hidden}
body{position:relative;background:var(--dark);font-family:Arimo,Arial,sans-serif;color:var(--text)}
.abs{position:absolute}
.top-strip{left:0;top:0;width:681px;height:15px;background:#1b1b1b;border-bottom:1px solid #888}
.header{left:0;top:16px;width:681px;height:298px;background:linear-gradient(90deg,var(--header-b),var(--header-a) 30%,#e6e6e6 55%,var(--header-a) 75%,var(--header-b))}
.notch{left:310px;top:312px}
.brand-mark{left:326px;top:30px;width:30px;height:30px;background:var(--orange)}
.brand{left:0;top:86px;width:681px;text-align:center;font-family:"PT Sans Narrow",sans-serif;font-weight:700;font-size:13px;letter-spacing:1.5px;color:var(--head);line-height:15px}
.main-nav{left:0;top:139px;width:681px;display:flex;justify-content:center;gap:4px;font-size:7.5px;color:#222}
.main-nav span{padding:0 5px}
.main-nav i{display:inline-block;width:1px;height:30px;background:#333;transform:rotate(28deg);margin-top:-11px}
.tagline{left:106px;top:173px;width:469px;text-align:center;font-family:"PT Sans Narrow",sans-serif;font-weight:700;font-size:13.5px;line-height:17.5px;color:#3a3a3a;text-transform:uppercase}
.books{left:0;top:234px;width:681px;text-align:center;font-family:Ubuntu,sans-serif;font-weight:700;font-size:64px;letter-spacing:-2px;color:#222;text-shadow:0 2px 2px rgba(0,0,0,.35)}
.lower-band{left:0;top:876px;width:681px;height:324px;background:var(--dark-2)}
.panel{left:98px;top:334px;width:485px;height:788px;background:var(--panel)}
.serif-head{font-family:"Noto Serif",serif;font-size:10.5px;color:var(--orange);white-space:nowrap}
.copy{font-size:6.3px;line-height:7.7px;color:var(--text)}
.copy em{font-style:normal;color:var(--orange)}
.tooltip{background:#f7f7f7;border-radius:3px;box-shadow:0 1px 3px rgba(0,0,0,.3);font-size:5.5px;color:#333;padding:3px 9px}
.slideshow{left:316px;top:6px;width:146px;height:150px;background:var(--orange)}
.slide-frame{left:6px;top:6px;width:134px;height:102px;border:1px solid #f6c3a8}
.slide-question{left:7px;top:8px;width:118px;font-family:"Open Sans",sans-serif;font-weight:800;font-size:11px;line-height:12px;color:var(--white)}
.call-button{left:0;top:115px;width:146px;text-align:center;font-family:"Open Sans",sans-serif;font-weight:800;font-size:7.6px;line-height:12px;color:var(--white);letter-spacing:.3px}
.call-button b{font-size:9.5px;letter-spacing:.5px}
.sub-head{font-size:9.5px;color:var(--orange);font-weight:400}
.checklist{list-style:none;font-size:6.3px;color:var(--text)}
.checklist li{position:relative;padding-left:19px;line-height:7.5px;margin-bottom:3.3px}
.checklist li::before{content:"";position:absolute;left:3px;top:0;width:7px;height:7px;background:#eee;border:1px solid #bbb}
.checklist li.on::after{content:"";position:absolute;left:5px;top:0;width:3px;height:5px;border-right:1.3px solid #222;border-bottom:1.3px solid #222;transform:rotate(40deg)}
.checklist li.hl{color:var(--orange)}
.map{left:315px;top:269px;width:146px;height:111px;background:linear-gradient(#f4f4f4,#e8e8e8);border:1px solid #ccc}
.divider{left:9px;top:692px;width:466px;height:1px;background:#f3f3f3}
.divider-dot{left:236px;top:688px;width:9px;height:9px;border-radius:50%;background:var(--panel);border:1px solid #f3f3f3}
.partner-name{left:118px;top:726px;width:130px;height:24px;background:var(--white);border:1px solid #bbb;text-align:center;font-size:11px;font-weight:700;line-height:22px;color:#6b1010}
.panel-dot{left:236px;top:783px;width:8px;height:8px;border-radius:50%;background:var(--white)}
.foot-nav{left:0;top:1135px;width:681px;display:flex;justify-content:center;gap:14px;font-size:7px;color:#ddd}
.copyright{left:0;top:1183px;width:681px;text-align:center;font-size:6.3px;color:#ccc}
</style>
</head>
<body>
<div class="abs top-strip"></div>
<header class="abs header"></header>
<svg class="abs notch" width="62" height="12" viewBox="0 0 62 12"><path d="M0 2 H20 L31 10 L42 2 H62" fill="none" stroke="#555" stroke-width="2"/></svg>

<span class="abs brand-mark"></span>
<div class="abs brand">LINDEN &amp; CRANE<br>BOOKKEEPING</div>

<nav class="abs main-nav">
  <span>HOME</span><i></i><span>ABOUT US</span><i></i><span>SERVICES</span><i></i><span>TESTIMONIALS</span><i></i><span>ARTICLES</span><i></i><span>ENDORSEMENTS</span><i></i><span>LINKS</span><i></i><span>CONTACT US</span>
</nav>

<p class="abs tagline">For nearly 10 years Linden &amp; Crane has been servicing the local &amp; inter-state communities of Australia, providing first-class BAS &amp; bookkeeping services with apersonal touch unmatched by anyone else</p>

<div class="abs books">Books</div>

<div class="abs lower-band"></div>

<main class="abs panel">
  <h2 class="abs serif-head" style="left:12px;top:11px">Welcome to Linden &amp; Crane</h2>
  <p class="abs copy" style="left:14px;top:32px;width:266px">Lorem ipsum dolor sit amet, consectetur adipiscing elit. Praesent eu nulla vitae elit interdum sagittis eget a leo. Aenean et mauris massa. Proin feugiat risus id metus laoreet at condimentum metus pharetra. Ut <em>sollicitudin</em> dolor sit amet libero scelerisque quis vestibulum nibh rhoncus. Etiam est nibh, feugiat porta porta sed, blandit at est. Aenean facilisis dui viverra lectus viverra iaculis.Lorem ipsum dolor sit amet, consectetur adipiscing elit. Praesent eu nulla vitae elit interdum sagittis eget a leo. Aenean et mauris massa. Proin feugiat risus id metus laoreet at condimentum metus pharetra. Ut <em>sollicitudin</em> dolor sit amet libero scelerisque quis vestibulum nibh rhoncus. Etiam est nibh, feugiat porta porta sed, blandit at est. Aenean facilisis dui viverra lectus viverra iaculis.</p>
  <div class="abs tooltip" style="left:102px;top:58px">Tooltip goes here</div>

  <aside class="abs slideshow">
    <div class="abs slide-frame"><p class="abs slide-question">IS YOUR PAPERWORK IN A MESS?</p></div>
    <div class="abs call-button">CALL LINDEN &amp; CRANE NOW<br><b>03 7482 9163</b></div>
  </aside>

  <h3 class="abs sub-head" style="left:14px;top:147px">To summarise</h3>
  <ul class="abs checklist" style="left:17px;top:172px;width:190px">
    <li>Lorem ipsum dolor sit amet</li><li class="on">Consectetur adipiscing elit. Praesent</li><li class="on">Mnulla vitae elit interdum sagittis eget</li><li>Aenean et mauris massa. Proin feugiat risus id metus</li><li>Lorem ipsum dolor sit amet</li><li>Proin feugiat risus id metus laoreet at</li><li>Consectetur adipiscing elit. Praesent eu nulla vitae elit interdum sagittis eget a leo. Aenean et mauris massa.</li>
  </ul>
  <ul class="abs checklist" style="left:204px;top:172px;width:190px">
    <li>Lorem ipsum dolor sit amet</li><li class="on">Consectetur adipiscing elit. Praesent</li><li class="on">Mnulla vitae elit interdum sagittis eget</li><li>Aenean et mauris massa. Proin feugiat risus id metus</li><li>Lorem ipsum dolor sit amet</li><li>Proin feugiat risus id metus laoreet at</li><li>Consectetur adipiscing elit. Praesent eu nulla vitae elit interdum sagittis eget a leo. Aenean et mauris massa.</li>
  </ul>

  <h2 class="abs serif-head" style="left:12px;top:272px">Welcome to Linden &amp; Crane</h2>
  <ul class="abs checklist" style="left:17px;top:296px;width:200px">
    <li>Lorem ipsum dolor sit amet</li><li class="on hl">Consectetur adipiscing elit. Praesent</li><li class="on hl">Mnulla vitae elit interdum sagittis eget</li><li>Aenean et mauris massa. Proin feugiat risus id metus</li><li>Lorem ipsum dolor sit amet</li><li>Proin feugiat risus id metus laoreet at</li><li>Consectetur adipiscing elit. Praesent eu nulla vitae elit interdum sagittis eget a leo. Aenean et mauris massa.</li>
  </ul>
  <div class="abs map" role="img" aria-label="Map of Australia marking office locations"></div>

  <div class="abs copy" style="left:32px;top:398px;width:262px">
    <p style="margin-bottom:7px">Lorem ipsum dolor sit amet, consectetur adipiscing elit. Praesent eu nulla vitae elit interdum sagittis eget a leo. Aenean et mauris massa. Proin feugiat risus id metus laoreet at condimentum metus pharetra. Ut sollicitudin dolor sit amet libero scelerisque quis vestibulum nibh rhoncus. Etiam est nibh, feugiat porta porta sed, blandit at est. Aenean facilisis dui viverra lectus viverra <em>iaculis.Lorem ipsum</em> dolor sit amet, consectetur adipiscing elit. Praesent eu nulla vitae elit interdum sagittis eget a leo. Aenean et mauris massa. Proin feugiat risus id metus laoreet at condimentum metus pharetra. Ut sollicitudin dolor sit amet libero scelerisque quis vestibulum nibh rhoncus. Etiam est nibh, feugiat porta porta sed, blandit at est. Aenean facilisis dui viverra lectus viverra iaculis.</p>
    <p style="margin-bottom:7px">Lorem ipsum dolor sit amet, consectetur adipiscing elit. Praesent eu nulla vitae elit interdum sagittis eget a leo. Aenean et mauris massa. Proin</p>
    <p style="margin-bottom:7px">feugiat risus id metus laoreet at condimentum metus pharetra. Ut sollicitudin dolor sit amet libero scelerisque quis vestibulum nibh rhoncus. Etiam est nibh, feugiat porta porta sed, blandit at est. Aenean facilisis dui viverra lectus viverra iaculisfeugiat porta porta sed, blandit at est. Aenean facilisis dui viverra lectus viverra iaculis.</p>
    <p style="width:216px">.Lorem ipsum dolor sit amet, consectetur adipiscing elit. Praesent eu nulla vitae elit interdum sagittis eget a leo. giat risus id metus laoreet at condimentum metus pharetra. Ut sollicitudin dolor sit amet libero scelerisque quis vestibulum nibh rhoncus. Etiam est nibh, .Lorem ipsum dolor sit amet, consectetur adipiscing elit. Praesent eu nulla vitae elit interdum sagittis eget a leo. Aenean et mauris massa. Proin feugiat risus id metus laoreet e quis vestibulum .Lorem ipsum dolor sit amet, consectetur adipiscing elit. Praesent eu nulla vitae elit interdum sagittis eget a leo. Aenean et mauris massa. Proin feugiat risus id metus laoreet at condimentum metus pharetra. Ut sollicitudin dolor sit amet libero scelerisque quis vestibulum nibh rhoncus. Etiam est nibh, rhoncus. Etiam est nibh,</p>
  </div>
  <div class="abs tooltip" style="left:92px;top:415px">Tooltip goes here</div>

  <h2 class="abs serif-head" style="left:312px;top:413px">Welcome to Linden &amp; Crane</h2>
  <ul class="abs checklist" style="left:319px;top:436px;width:150px">
    <li>Lorem ipsum dolor sit amet</li><li class="on">Consectetur adipiscing elit. Praesent</li><li class="on">Mnulla vitae elit interdum sagittis eget</li><li>Aenean et mauris massa. Proin feugiat</li><li>Lorem ipsum dolor sit amet</li><li>Proin feugiat risus id metus laoreet at</li><li>Consectetur adipiscing elit. Praesent eu nulla vitae elit interdum sagittis eget a leo.</li>
  </ul>

  <div class="abs divider"></div>
  <div class="abs divider-dot"></div>

  <div class="abs" style="left:22px;top:710px;width:38px;height:64px;background:#2b4a8a"></div>
  <div class="abs" style="left:76px;top:714px;width:28px;height:50px;background:#e8e8e8;border:1px solid #bbb"></div>
  <div class="abs partner-name">Linden &amp; Crane</div>
  <div class="abs" style="left:260px;top:706px;width:66px;height:68px;background:#f2f2f2;border:1px solid #bbb"></div>
  <div class="abs" style="left:339px;top:718px;width:130px;height:44px;background:#f7f7f7;border:1px solid #bbb"></div>

  <div class="abs panel-dot"></div>
</main>

<nav class="abs foot-nav">
  <span>HOME</span><span>ABOUT US</span><span>SERVICES</span><span>TESTIMONIALS</span><span>ARTICLES</span><span>ENDORSEMENTS</span><span>LINKS</span><span>CONTACT US</span>
</nav>
<p class="abs copyright">copyright @ lindencrane.com.au 2012</p>
</body>
</html>
```